Harvest Gathering event flyer

I would like a church event flyer designed. The event is called "HARVEST GATHERING 2018". I am looking for a professional, yet catchy design that uses our brand colors and logo creatively while communicating key information of the event effectively.

1. The logo is attached in two color formats. The designer has the choice to use them as he/she want.

2. The location of the event is: Lindqvist Community Center, 482 Tamsworth Street, Portland, ME 04102
3. Time and date of event. The designer can organize and format the date and time as he/she pleases.
December 28th, 29th @ 7:00PM
December 30th @ 10:00AM
4. The topic of the event is "Tongues of fire". The designer is free to use this phrase as he/she pleases to create a good composition.
5. Speaker: Prophet Marcus Obuya
6. Contact information: contact@cedarbrookfellowship.org - Telephone number: 207 555 0148

7. I would also like the following three words on the flyer. These words describe the focus of the event: FIRE, REVIVAL, PROPHETIC

```html
<!DOCTYPE html>
<html lang="en">
<head>
<meta charset="UTF-8">
<title>Harvest Gathering 2018 – Tongues of Fire</title>
<link href="https://fonts.googleapis.com/css2?family=Cinzel:wght@400;700&family=Bitter:ital,wght@0,700;1,700&family=Lato:ital,wght@0,400;1,700&display=swap" rel="stylesheet">
<style>
  :root{
    --page:#f4f4f4;
    --navy:#0b1d5a;
    --navy-deep:#06123f;
    --fire:#ff8a1c;
    --ink:#120d05;
    --parchment-edge:#9a5a1c;
    --date-ink:#3a1c05;
    --contact:#f6a12a;
    --white:#ffffff;
    --book:#3a1a10;
  }
  html,body{margin:0;padding:0;width:1200px;height:1198px;overflow:hidden;background:var(--page);}
  .flyer{
    position:absolute;left:155px;top:25px;width:966px;height:1248px;
    transform:scale(0.92);transform-origin:top left;overflow:hidden;
    background:
      radial-gradient(ellipse 300px 260px at 50% 30%, rgba(255,230,140,.95), rgba(255,140,30,.85) 45%, rgba(255,120,20,0) 100%),
      radial-gradient(ellipse 520px 420px at 50% 38%, rgba(230,100,20,.9), rgba(200,80,20,0) 100%),
      radial-gradient(ellipse 560px 260px at 50% 66%, rgba(159,220,110,.9), rgba(111,211,214,.55) 55%, rgba(111,211,214,0) 100%),
      linear-gradient(180deg, var(--navy) 0%, #13307a 50%, var(--navy) 82%, var(--navy-deep) 100%);
    box-shadow:0 10px 30px rgba(0,0,0,.25);
  }
  .brand{position:absolute;left:76px;top:92px;display:flex;align-items:center;gap:10px;}
  .brand-mark{width:18px;height:18px;border-radius:50%;background:var(--fire);}
  .brand-name{font-family:'Cinzel',serif;font-weight:400;font-size:30px;line-height:1;color:var(--white);}
  .event-name{position:absolute;right:74px;top:92px;margin:0;white-space:nowrap;
    font-family:'Bitter',serif;font-weight:700;font-size:36px;line-height:1;letter-spacing:1.5px;color:var(--white);
    text-shadow:0 2px 4px rgba(0,0,0,.6);}
  .focus{position:absolute;left:0;right:0;top:268px;text-align:center;margin:0;
    font-family:'Bitter',serif;font-style:italic;font-weight:700;font-size:28px;letter-spacing:3px;color:var(--ink);}
  .book-art{position:absolute;left:256px;top:518px;width:570px;height:295px;border-radius:14px;
    background:radial-gradient(ellipse at 50% 20%, #6a2e14, var(--book) 70%);}
  .hand-art{position:absolute;left:470px;top:650px;width:110px;height:170px;border-radius:55px 55px 10px 10px;
    background:linear-gradient(180deg,#d88a4e,#b0653a);opacity:.8;}
  .topic{position:absolute;left:0;right:0;top:330px;margin:0;text-align:center;
    font-family:'Cinzel',serif;font-weight:700;color:var(--white);line-height:1;
    text-shadow:0 4px 10px rgba(0,0,0,.55);}
  .topic .line1{display:block;font-size:168px;letter-spacing:-6px;}
  .topic .line2{display:block;margin-top:-18px;padding-left:150px;}
  .topic .of{font-size:120px;letter-spacing:-6px;}
  .topic .fire{font-size:196px;letter-spacing:-8px;}
  .speaker{position:absolute;left:0;right:0;top:838px;text-align:center;margin:0;
    font-family:'Lato',sans-serif;font-style:italic;font-weight:700;font-size:36px;color:var(--ink);}
  .banner{position:absolute;left:58px;top:918px;width:870px;height:155px;}
  .dates{position:absolute;left:0;right:0;top:940px;text-align:center;margin:0;
    font-family:'Bitter',serif;font-weight:700;font-size:38px;line-height:48px;color:var(--date-ink);}
  .dates sup{font-size:22px;}
  .address{position:absolute;left:0;right:0;top:1102px;text-align:center;margin:0;
    font-family:'Lato',sans-serif;font-size:28px;color:var(--white);}
  .contact{position:absolute;left:0;right:0;top:1148px;display:flex;justify-content:center;gap:48px;margin:0;
    font-family:'Bitter',serif;font-weight:700;font-size:28px;color:var(--contact);}
</style>
</head>
<body>
<main class="flyer">
  <div class="brand"><span class="brand-mark"></span><span class="brand-name">Cedarbrook</span></div>
  <h2 class="event-name">HARVEST GATHERING 2018</h2>
  <p class="focus">FIRE. REVIVAL. PROPHETIC.</p>
  <div class="book-art" role="img" aria-label="Open leather-bound Bible held up by a hand, glowing with fire and smoke"></div>
  <div class="hand-art" role="img" aria-label="Hand raising the Bible"></div>
  <h1 class="topic"><span class="line1">TONGUES</span><span class="line2"><span class="of">OF</span><span class="fire">FIRE</span></span></h1>
  <p class="speaker">Speaker: Prophet Marcus Obuya</p>
  <svg class="banner" viewBox="0 0 870 155" role="img" aria-label="Parchment scroll banner">
    <defs>
      <linearGradient id="parch" x1="0" y1="0" x2="0" y2="1">
        <stop offset="0" stop-color="#f7d27a"/><stop offset=".5" stop-color="#f0b545"/><stop offset="1" stop-color="#c9822a"/>
      </linearGradient>
    </defs>
    <path d="M0 30 L90 20 L90 140 L10 150 L40 90 Z" fill="var(--parchment-edge)"/>
    <path d="M870 30 L780 20 L780 140 L860 150 L830 90 Z" fill="var(--parchment-edge)"/>
    <path d="M70 15 Q435 -5 800 15 L800 140 Q435 120 70 140 Z" fill="url(#parch)"/>
  </svg>
  <p class="dates">December 28<sup>th</sup>, 29<sup>th</sup> @ 7:00PM<br>December 30<sup>th</sup> @ 10:00AM</p>
  <p class="address">Lindqvist Community Center, 482 Tamsworth Street, Portland, ME 04102</p>
  <p class="contact"><span>contact@cedarbrookfellowship.org</span><span>Tel. 207 555 0148</span></p>
</main>
</body>
</html>
```